White Paper and One-Page Advertisement for TELVAMORE-QX

I need both documents to be better formatted and designed so they look professional, not something someone with mediocre word skills put together. They will go out to 1000s of industry professionals, and they need to look sharp. I need them to have my company's color palate logo, and branding on it similar to how it is now, but better. Please do not change any of the written content, but it can be arranged in any other format you think is better. Smart art and things i've already used can be omitted in favor of better designs. The developer is free to use their creativity. White paper should not be longer than the three pages unless necessary.

Target Market(s)

Life Sciences supply chain professionals

Colors
33b8a4
0592cd
9bcb3c
fbee3e
3277b5

Requirements
Must have
• Must be professional looking and not look like something done in word. Please use the color palate as seen on the documents.
Should not have
• Any changes to the written content.

```html
<!DOCTYPE html>
<html lang="en">
<head>
<meta charset="utf-8">
<title>Changing Pharma's Paradigm of Waste — White Paper Cover</title>
<link rel="stylesheet" href="https://fonts.googleapis.com/css2?family=Exo+2:wght@300;400;800&display=swap">
<style>
  :root {
    --stage: #2b2b2b;
    --paper: #ffffff;
    --teal: #1b8472;
    --green: #8dc63f;
    --green-light: #9fd04a;
    --green-deep: #4fa64a;
    --ink-white: #ffffff;
  }
  html, body {
    margin: 0;
    padding: 0;
    width: 1200px;
    height: 1200px;
    overflow: hidden;
    background: var(--stage);
  }
  .cover {
    position: absolute;
    left: 196px;
    top: 30px;
    width: 807px;
    height: 1140px;
    display: block;
  }
  .cover-text { font-family: "Exo 2", sans-serif; }
  .title-lead { font-weight: 300; fill: var(--teal); }
  .title-main { font-weight: 800; fill: var(--teal); }
  .subtitle { font-weight: 400; fill: var(--ink-white); }
  .author, .date, .brand-name { font-weight: 800; fill: var(--teal); }
</style>
</head>
<body>
<svg class="cover" viewBox="0 0 945 1335" xmlns="http://www.w3.org/2000/svg">
  <defs>
    <clipPath id="page-clip"><rect width="945" height="1335"/></clipPath>
    <linearGradient id="corner-gradient" x1="0" y1="1" x2="1" y2="0">
      <stop offset="0" stop-color="var(--green-deep)"/>
      <stop offset="1" stop-color="var(--green-light)"/>
    </linearGradient>
    <radialGradient id="photo-ward" cx="0.5" cy="0.4" r="0.7">
      <stop offset="0" stop-color="#e8e2d6"/>
      <stop offset="0.6" stop-color="#b9b8ae"/>
      <stop offset="1" stop-color="#7d8580"/>
    </radialGradient>
    <radialGradient id="photo-ceremony" cx="0.45" cy="0.5" r="0.7">
      <stop offset="0" stop-color="#d9b98a"/>
      <stop offset="0.5" stop-color="#8a5a3a"/>
      <stop offset="1" stop-color="#3e2a22"/>
    </radialGradient>
  </defs>

  <g clip-path="url(#page-clip)">
    <rect class="page" width="945" height="1335" fill="var(--paper)"/>

    <!-- upper teal panel and corner accent -->
    <polygon class="panel-teal" points="245,0 688,0 945,300 945,840 600,840 420,200" fill="var(--teal)"/>
    <polygon class="corner-accent" points="715,0 945,0 945,272" fill="url(#corner-gradient)"/>

    <!-- lower green field -->
    <polygon class="field-green" points="386,732 945,732 945,1120 780,1335 0,1335 0,1257" fill="var(--green)"/>
    <polygon class="corner-white" points="790,1335 945,1335 945,1130" fill="var(--paper)"/>

    <!-- subtitle band -->
    <polygon class="band-teal" points="134,1075 945,1075 945,1153 77,1153" fill="var(--teal)"/>

    <!-- first photo circle -->
    <circle class="ring-teal" cx="351" cy="262" r="215" fill="var(--teal)"/>
    <g role="img" aria-label="Photograph: a smiling young patient sitting up in a hospital bed">
      <circle cx="351" cy="262" r="197" fill="url(#photo-ward)"/>
    </g>

    <!-- second photo circle -->
    <circle class="ring-white" cx="663" cy="596" r="308" fill="var(--paper)"/>
    <g role="img" aria-label="Photograph: a family helping a young man in traditional ceremonial dress">
      <circle cx="663" cy="596" r="286" fill="url(#photo-ceremony)"/>
    </g>

    <!-- brand -->
    <circle class="brand-mark" cx="181" cy="597" r="40" fill="none" stroke="var(--teal)" stroke-width="5"/>
    <text class="cover-text brand-name" x="193" y="685" font-size="34" text-anchor="middle">TELVAMORE-QX</text>

    <!-- title -->
    <text class="cover-text title-lead" x="571" y="997" font-size="50" text-anchor="middle">CHANGING PHARMA’S</text>
    <text class="cover-text title-main" x="571" y="1054" font-size="58" text-anchor="middle" letter-spacing="1">PARADIGM OF WASTE</text>

    <text class="cover-text subtitle" x="511" y="1107" font-size="24" text-anchor="middle">How Pharma’s Demand Volatility Could Be Costing</text>
    <text class="cover-text subtitle" x="511" y="1134" font-size="24" text-anchor="middle">You Millions in Material Write-downs &amp; Procurement</text>

    <text class="cover-text author" x="493" y="1215" font-size="40" text-anchor="middle">Dale Marwick</text>
    <text class="cover-text date" x="476" y="1292" font-size="58" text-anchor="middle">AUGUST 2018</text>
  </g>
</svg>
</body>
</html>
```